Pharmacist turned chef in Key West Fl needs a logo design

I am looking for a professional looking business card that says who I am and what I do. For example Chef Dale Morvik, natural organic and health supportive cooking. Phone 555-416-8870 email dalemorvik@quillpost.example web www.thesaltedharvest.example, Key West fl. The color or colors should have some green and other colors that look good together that stimulate appetite and give a clean healthy image. To help with a thought process, words like food as medicine, medicine is food, good nutrition is health but at the same time I do not want a lot of medical symbols that me it look clinical. Any questions please contact me.

```html
<!DOCTYPE html>
<html lang="en">
<head>
<meta charset="utf-8">
<title>Chef Dale Morvik – Business Card</title>
<link rel="stylesheet" href="https://fonts.googleapis.com/css2?family=Open+Sans:wght@300;400;700&display=swap">
<style>
  :root {
    --lime: #b1ca06;
    --orange: #ef813f;
    --ink: #222222;
    --icon-green: #7cbd3b;
    --paper: #ffffff;
    --frame: #1c1c1c;
    --ghost: #ededed;
  }
  html, body {
    margin: 0;
    padding: 0;
    overflow: hidden;
    background: var(--paper);
  }
  .canvas {
    position: relative;
    width: 1200px;
    height: 780px;
    box-sizing: border-box;
    border: 2px solid var(--frame);
    background: var(--paper);
    font-family: "Open Sans", sans-serif;
    color: var(--ink);
    overflow: hidden;
  }
  .card {
    position: absolute;
    left: 56px;
    top: 54px;
    width: 1087px;
    height: 671px;
    box-sizing: border-box;
    border: 2px solid var(--frame);
    overflow: hidden;
    background: var(--paper);
  }
  .band-top {
    position: absolute;
    left: 0; top: 0;
    width: 100%;
    height: 140px;
    background: var(--lime);
  }
  .band-title {
    position: absolute;
    left: 0; top: 140px;
    width: 100%;
    height: 196px;
    background: var(--orange);
  }
  .band-rule {
    position: absolute;
    left: 0; top: 336px;
    width: 100%;
    height: 22px;
    background: var(--lime);
  }
  .brand-mark {
    position: absolute;
    left: 112px;
    top: 172px;
    width: 118px;
    height: 132px;
    display: flex;
    flex-direction: column;
    align-items: center;
    justify-content: center;
    gap: 8px;
    text-align: center;
  }
  .brand-mark .dot {
    width: 22px;
    height: 22px;
    border-radius: 50%;
    background: var(--paper);
  }
  .brand-mark .brand-name {
    font-size: 20px;
    font-weight: 700;
    line-height: 1.1;
    color: var(--paper);
  }
  .headline {
    position: absolute;
    left: 247px;
    top: 196px;
    margin: 0;
    font-weight: 400;
    line-height: 1;
  }
  .headline .light {
    display: block;
    font-size: 45px;
    font-weight: 300;
    letter-spacing: 0.5px;
  }
  .headline .bold {
    display: block;
    margin-top: 9px;
    font-size: 45px;
    font-weight: 700;
    letter-spacing: 0.5px;
  }
  .ghost-name {
    position: absolute;
    left: 112px;
    top: 400px;
    width: 260px;
    font-size: 52px;
    font-weight: 700;
    line-height: 1.05;
    text-align: center;
    color: var(--ghost);
  }
  .chef-name {
    position: absolute;
    left: 62px;
    top: 508px;
    margin: 0;
    font-size: 37px;
    font-weight: 700;
    letter-spacing: -0.3px;
  }
  .contacts {
    position: absolute;
    left: 453px;
    top: 432px;
    margin: 0;
    padding: 0;
    list-style: none;
  }
  .contacts li {
    display: flex;
    align-items: center;
    height: 67px;
    font-size: 33px;
  }
  .contacts .icon {
    width: 35px;
    height: 35px;
    margin-right: 24px;
    flex: none;
  }
</style>
</head>
<body>
  <div class="canvas">
    <div class="card">
      <div class="band-top"></div>
      <div class="band-title"></div>
      <div class="band-rule"></div>

      <div class="brand-mark">
        <span class="dot"></span>
        <span class="brand-name">Salted<br>Harvest</span>
      </div>

      <h1 class="headline">
        <span class="light">NATURAL ORGANIC AND</span>
        <span class="bold">HEALTH SUPPORTIVE COOKING</span>
      </h1>

      <div class="ghost-name" aria-hidden="true">Salted<br>Harvest</div>

      <p class="chef-name">Chef Dale Morvik</p>

      <ul class="contacts">
        <li>
          <svg class="icon" viewBox="0 0 36 36" aria-hidden="true">
            <rect width="36" height="36" rx="6" fill="var(--icon-green)"/>
            <path d="M12 8 l4 0 l2 6 l-3 2 q2 5 6 7 l2 -3 l6 2 l0 4 q-1 3 -4 3 q-10 -1 -15 -12 q-1 -6 2 -9z" fill="var(--ink)"/>
          </svg>
          555-416-8870
        </li>
        <li>
          <svg class="icon" viewBox="0 0 36 36" aria-hidden="true">
            <rect width="36" height="36" rx="6" fill="var(--icon-green)"/>
            <rect x="7" y="10" width="22" height="16" fill="var(--ink)"/>
            <path d="M7 10 L18 19 L29 10" fill="none" stroke="var(--icon-green)" stroke-width="1.6"/>
          </svg>
          dalemorvik@quillpost.example
        </li>
        <li>
          <svg class="icon" viewBox="0 0 36 36" aria-hidden="true">
            <rect width="36" height="36" rx="6" fill="var(--icon-green)"/>
            <g fill="none" stroke="var(--ink)" stroke-width="1.4">
              <circle cx="18" cy="18" r="10"/>
              <ellipse cx="18" cy="18" rx="4.5" ry="10"/>
              <line x1="8" y1="18" x2="28" y2="18"/>
              <line x1="18" y1="8" x2="18" y2="28"/>
              <line x1="10" y1="13" x2="26" y2="13"/>
              <line x1="10" y1="23" x2="26" y2="23"/>
            </g>
          </svg>
          www.thesaltedharvest.example
        </li>
      </ul>
    </div>
  </div>
</body>
</html>
```